Canvassing technical expertise for co-ownerships

Good morning,
The KORU company specializes in real estate expertise. We would like to create a flyer to attract new customers. Our main target is condominium trustees and co-ownerships.
We want a double-sided A4 format. The language used must be French. The flyer must come as close as possible to the graphic charter of our website (title font “brandon grotesque”; text font “avenir light”; green color code “#2A7C6F”, beige “#FFFDF8”, possibly with the following nuances in the theme: #95BDB6; #2C8D7E). The site is accessible at the following address: https://www.koru-batim.fr/.
Our logo must be accompanied by the phrase “Experts at the service of co-ownership!”.
The flyer must convey the main information from the website, emphasizing:
- All the missions offered (see “Our services” page of the website)
- We operate throughout the French national territory, with teams spread across the territory.
- A short text about our history (“about” page of the site)
- Making contact, by email contact@saskoru.fr or by telephone 06.71.29.84.52.

Our postal address should appear more discreetly at the bottom of the page, in the form “SAS KORU, 57 Rue des Tilleuls, 34 400 LUNEL”

Condominium associations and co-ownerships

Expertise du bâtiment

• police titres « brandon grotesque » ; police texte « avenir light »

• All the characteristics requested in the project description. The language used must be French.
• A neat and serious general appearance
• Not intended to be entertaining, funny, too colorful, etc.

```html
<!DOCTYPE html>
<html lang="fr">
<head>
<meta charset="utf-8">
<title>KORU – Expertise immobilière</title>
<link rel="stylesheet" href="https://fonts.googleapis.com/css2?family=Nunito+Sans:wght@300;400&family=Outfit:wght@500;600&display=swap">
<style>
  :root {
    --green: #2a7c6f;
    --green-soft: rgba(42, 124, 111, 0.82);
    --paper: #ffffff;
    --backdrop: #b4b4b4;
    --ink: #333333;
    --mark-grey: #e6e6e6;
    --title-font: "Outfit", "Helvetica Neue", Arial, sans-serif;
    --text-font: "Nunito Sans", "Avenir", Arial, sans-serif;
  }
  * { margin: 0; padding: 0; box-sizing: border-box; }
  html, body { width: 726px; height: 1200px; overflow: hidden; }
  body { background: var(--backdrop); position: relative; font-family: var(--text-font); color: var(--ink); }

  .page {
    position: absolute; left: 172px; width: 383px; height: 542px;
    background: var(--paper); overflow: hidden;
  }
  .page--presentation { top: 39px; }
  .page--services { top: 610px; }

  .brand { position: absolute; top: 28px; left: 93px; width: 220px; height: 84px; }
  .brand__square { position: absolute; left: 0; top: 0; width: 73px; height: 83px; background: var(--mark-grey); }
  .brand__name {
    position: absolute; left: 84px; top: 8px;
    font-family: var(--text-font); font-weight: 400; font-size: 58px; line-height: 60px;
    color: var(--green); letter-spacing: 2px;
  }
  .brand__tagline {
    position: absolute; left: 80px; top: 73px;
    font-family: var(--text-font); font-weight: 400; font-size: 5.6px; letter-spacing: 2.2px;
    color: var(--green); white-space: nowrap;
  }

  .photo { position: absolute; left: 0; width: 383px; }
  .photo--buildings {
    top: 116px; height: 161px;
    background: linear-gradient(90deg, #a99a82 0%, #4d6d8f 35%, #3a3d44 55%, #7d7872 78%, #9a948c 100%);
  }
  .photo__tint { position: absolute; left: 0; bottom: 0; width: 180px; height: 32px; background: var(--green-soft); }
  .photo--worksite {
    top: 300px; height: 171px;
    background: linear-gradient(120deg, #cfd76a 0%, #e8e6df 30%, #b9b8b2 55%, #d8dab8 80%, #c9d35c 100%);
  }

  .section-title {
    position: absolute; height: 25px; background: var(--green); color: #fff;
    font-family: var(--title-font); font-weight: 500; font-size: 11.5px; line-height: 25px;
    padding-left: 9px; white-space: nowrap;
  }
  .page--presentation .section-title { left: 20px; top: 277px; width: 160px; }
  .page--services .section-title { left: 0; top: 133px; width: 200px; padding-left: 29px; }

  .body-text { position: absolute; left: 29px; width: 326px; font-size: 6.6px; line-height: 9.2px; font-weight: 300; }
  .body-text p + p { margin-top: 9.2px; }
  .page--presentation .body-text { top: 306px; }
  .page--services .body-text { top: 164px; }

  .services-list { list-style: none; margin-top: 13px; font-size: 6.8px; line-height: 11.5px; }

  .contact-band {
    position: absolute; left: 0; top: 502px; width: 383px; height: 31px;
    background: var(--green); color: #fff; text-align: center;
    font-size: 6.4px; line-height: 9px; padding-top: 6px; font-weight: 300;
  }
</style>
</head>
<body>

<section class="page page--presentation">
  <div class="brand">
    <div class="brand__square"></div>
    <div class="brand__name">KORU</div>
    <div class="brand__tagline">EXPERTISE IMMOBILIERE</div>
  </div>

  <div class="photo photo--buildings" role="img" aria-label="Photographie de façades d'immeubles résidentiels avec balcons">
    <div class="photo__tint"></div>
  </div>

  <h2 class="section-title">Présentation de l’entreprise</h2>

  <div class="body-text">
    <p>Afin de se faire connaître nous avons préparé un texte de présentation qui est le suivant :</p>
    <p>« KORU est le partenaire de confiance des syndicats de copropriété et des copropriétaires.</p>
    <p>Fondée en 2019, KORU joue un rôle essentiel sur l’ensemble des enjeux techniques des copropriétés.</p>
    <p>Chez KORU, nous offrons un accompagnement technique complet aux syndics de copropriété et aux copropriétaires en apportant une expertise pointue sur le bâti et en les soutenant à chaque étape de leur projet. Avec aujourd’hui un réseau de plus d’une soixantaine de collaborateurs, nous sommes fiers de proposer une gamme complète de services spécialisés pour assister nos clients dans les étapes clés de la vie de leur immeuble.</p>
    <p>Avec une présence nationale, notre équipe de plus d’une soixantaine d’intervenants est prête à répondre à vos besoins, où que vous soyez. »</p>
    <p>Chez KORU, nous sommes animés par la passion de fournir des solutions sur mesure et de qualité à nos clients. Nous nous engageons à être à l’écoute de leurs besoins et à leur offrir un service irréprochable à chaque étape de leur parcours avec nous.</p>
  </div>

  <footer class="contact-band">
    06.71.29.84.52 | mail contact@saskoru.fr<br>
    SAS KORU, 57 Rue des Tilleuls, 34 400 LUNEL
  </footer>
</section>

<section class="page page--services">
  <div class="brand">
    <div class="brand__square"></div>
    <div class="brand__name">KORU</div>
    <div class="brand__tagline">EXPERTISE IMMOBILIERE</div>
  </div>

  <h2 class="section-title">Les services que nous offrons</h2>

  <div class="body-text">
    <p>Nous voudrions aussi présenter les prestations que nous proposons et qui sont les suivantes :</p>
    <ul class="services-list">
      <li>- Assistance à la livraison</li>
      <li>- Suivi des levées de réserves et de la garantie de parfait achèvement</li>
      <li>- Visite d’immeuble</li>
      <li>- Audit de garantie décennale</li>
      <li>- Assistance technique garantie décennale</li>
      <li>- Expertise privée Audit technique du bâti</li>
      <li>- Diagnostic de performance énergétique (DPE)</li>
      <li>- PPT Plan Pluriannuel de Travaux</li>
    </ul>
  </div>

  <div class="photo photo--worksite" role="img" aria-label="Photographie d'intervenants en gilets de sécurité étudiant des plans sur un chantier"></div>

  <footer class="contact-band">
    06.71.29.84.52 | mail contact@saskoru.fr<br>
    SAS KORU, 57 Rue des Tilleuls, 34 400 LUNEL
  </footer>
</section>

</body>
</html>
```